Expanding Training Company needs a powerpoint template to deliver a consistent professional image

We want to start with a ppt template that is clean and flexible.
We are a small training organisation focusing on personal effectiveness, leadership, management and change. The MD is a New Zealander living in the United Kingdom and loves the idea of the clean green image that NZ has and wants the PowerPoint template to reflect that. We are pragmatic in what we do - everything comes back to performance improvement. Our clients are big players and our presentations need to be as clean, and as professional as theirs. We need a template that is versatile and can have their logos added as necessary.
Our training tends to be very current and as such we would like to use a lot of images and less words/bullets. We have company colours, logos and fonts that we are happy with and will continue to use.

Here are our company values to give you a sense of what we are about…

As a learning organisation we are always looking to continually improve and renew, our material, ideas, and methods, and are continually on the look out for new techniques, interventions and applications that provide measurable results to our clients.

We think life is about people and relationships, and we are prepared to walk away if people don't keep their word, are untrustworthy or lack integrity, as life is just too short to work with arses.
And because we are not arses we admit when we are wrong and make good on our commitments.

For our clients its all about performance and training is a performance enhancer, we aim to provide training excellence tin all its guises that delivers performance and happy clients.

We harness the value of the team, we believe in Interdependence.

We make life easier for our clients and each other.

Flexibility, innovation and future focus/vision are what our clients can count on us for.

Work is one of many of life's great facilitators, we recognise and value the others - its not just about work.

Industry/Entity Type

It Company

Font styles to use
Other font styles liked:
• Avenir Next

Colors
abd037
9bcb3c

Requirements
Must have
• A clean look with multiple options for inserting images, tables, videos, text boxes etc
• copyright information
Nice to have
• Slide masters

```html
<!DOCTYPE html>
<html lang="en">
<head>
<meta charset="utf-8">
<title>Training Template – Slide Overview</title>
<link rel="stylesheet" href="https://fonts.googleapis.com/css2?family=Nunito+Sans:wght@300;400;600&family=Oswald:wght@500&display=swap">
<style>
  :root {
    --green: #3aab37;
    --green-light: #8cc63f;
    --green-dark: #22a03a;
    --green-text: #2f9e3a;
    --white: #ffffff;
    --grey-text: #8a8a8a;
    --bar-track: #f3d9d2;
    --sky: #4d7fc2;
    --hill: #8b8a4a;
    --grass: #6b8a3a;
  }
  * { box-sizing: border-box; margin: 0; padding: 0; }
  html, body { width: 1200px; height: 1189px; overflow: hidden; background: var(--white); }
  body { position: relative; font-family: "Nunito Sans", "Avenir Next", sans-serif; font-weight: 300; }

  .slide { position: absolute; width: 392px; height: 219px; background: var(--white); overflow: hidden; box-shadow: 0 2px 6px rgba(0,0,0,.18); }
  .col-1 { left: 4px; } .col-2 { left: 404px; } .col-3 { left: 804px; }
  .row-1 { top: 4px; } .row-2 { top: 242px; } .row-3 { top: 479px; } .row-4 { top: 717px; } .row-5 { top: 954px; }

  .photo { position: absolute; }
  .photo--valley { background: linear-gradient(180deg, #9fb4c9 0%, #7f8c86 35%, #8d8a4c 60%, #5f7d32 100%); }
  .photo--lake { background: linear-gradient(180deg, #3f74c0 0%, #b9c7d3 30%, #4d6a3a 45%, #2e78b6 70%, #3c5d2d 100%); }
  .photo--coast { background: linear-gradient(180deg, #4f7fbf 0%, #7b8e6a 40%, #2fa3b0 65%, #e8e1c9 80%, #3f6b33 100%); }
  .photo--dusk { background: linear-gradient(180deg, #b37f96 0%, #8a6d8a 35%, #4a5a3e 70%, #2f4a26 100%); }
  .photo--peak { background: linear-gradient(180deg, #5a86c4 0%, #7b7d6a 40%, #4a6b34 70%, #3b5a6a 100%); }
  .photo--rocks { background: linear-gradient(180deg, #a3a69c 0%, #6e6f5c 45%, #7b6a4f 70%, #4c6a2e 100%); }
  .photo--sunset { background: linear-gradient(180deg, #6f87a8 0%, #e0a84a 40%, #3c5570 60%, #2a3d55 100%); }
  .photo--path { background: linear-gradient(180deg, #a9b9c9 0%, #7d8b6f 45%, #c9c2a8 65%, #5f7c34 100%); }
  .photo--golden { background: linear-gradient(180deg, #2d5fb8 0%, #8fb0dc 30%, #d9b52c 55%, #c98f1c 80%, #a86f18 100%); }
  .photo--waterfall { background: linear-gradient(90deg, #6d6b5e 0%, #d9dcd8 45%, #5f6e4a 70%, #3f5a2a 100%); }
  .photo--cliff { background: linear-gradient(180deg, #7a7e6a 0%, #4f6a34 50%, #556b3c 100%); }
  .photo--portrait { background: linear-gradient(180deg, #eceeed 0%, #c9cccc 40%, #3b4a5e 70%, #2c3a4e 100%); }
  .photo--frost { background: radial-gradient(circle at 60% 50%, #e9eef0 0%, #9aa69c 40%, #3d5a2c 80%, #243a1c 100%); }
  .photo--reflect { background: linear-gradient(180deg, #c7c9c6 0%, #6f7367 35%, #3a4a5a 55%, #7d8a96 75%, #3a3e42 100%); }
  .photo--meadow { background: linear-gradient(180deg, #6f86b3 0%, #b07aa8 30%, #8a6f9a 45%, #6f7a45 65%, #c7b63c 85%, #4a5a2a 100%); }
  .photo--lighthouse { background: linear-gradient(180deg, #2f6fb5 0%, #7fb1d8 45%, #2a6ea8 70%, #9b9070 100%); }
  .photo--snow { background: linear-gradient(180deg, #8ba9d0 0%, #e4e8ea 35%, #6a6e62 60%, #4d6a3a 100%); }

  .green-panel { position: absolute; background: linear-gradient(135deg, var(--green-light) 0%, var(--green) 55%, var(--green-dark) 100%); color: var(--white); }
  .green-band { position: absolute; background: linear-gradient(90deg, var(--green-light), var(--green) 50%, var(--green-dark)); color: var(--white); }

  .headline { color: var(--green-text); font-size: 17.6px; line-height: 1.22; letter-spacing: .1px; }
  .headline--center { text-align: center; }
  .headline--right { text-align: right; }
  .caption { font-size: 12.5px; line-height: 1.25; }
  .lorem { color: var(--grey-text); font-size: 6.8px; line-height: 2.6; }
  .section-title { color: var(--green-text); font-size: 11.5px; font-weight: 400; }

  .brand { position: absolute; display: flex; align-items: center; gap: 4px; font-weight: 400; line-height: 1; }
  .brand__dot { width: 10px; height: 10px; border-radius: 50%; }

  .skill { position: absolute; left: 36px; width: 110px; }
  .skill__label { font-size: 5.5px; color: #777; font-weight: 400; }
  .skill__track { position: relative; height: 3px; margin-top: 2px; background: var(--bar-track); }
  .skill__fill { height: 100%; background: var(--green); }
  .skill__value { position: absolute; left: 118px; top: 7px; font-size: 5.5px; color: #777; }
</style>
</head>
<body>

<!-- Slide 1 -->
<section class="slide col-1 row-1">
  <p class="headline headline--center" style="position:absolute;left:0;right:0;top:22px;padding:0 70px;">Flexibility, Innovation And Future Focus/Vision Are What Our Clients Can Count On Us For.</p>
  <div class="photo photo--valley" role="img" aria-label="Mountain valley with trees" style="left:0;top:128px;width:128px;height:91px;"></div>
  <div class="photo photo--dusk" role="img" aria-label="Hills at dusk with forest" style="left:132px;top:128px;width:128px;height:91px;"></div>
  <div class="photo photo--coast" role="img" aria-label="Turquoise bay with sandy beach" style="left:264px;top:128px;width:128px;height:91px;"></div>
</section>

<!-- Slide 2 -->
<section class="slide col-2 row-1">
  <div class="photo photo--rocks" role="img" aria-label="Rocky hillside" style="left:0;top:0;width:96px;height:72px;"></div>
  <div class="green-panel caption" style="left:99px;top:0;width:95px;height:72px;display:flex;align-items:center;justify-content:center;text-align:center;font-size:9px;padding:6px;">We Think Life Is About People And Relationships</div>
  <div class="photo photo--valley" role="img" aria-label="Grassy valley with trees" style="left:0;top:75px;width:194px;height:144px;"></div>
  <div class="photo photo--peak" role="img" aria-label="Mountain peak above a lake" style="left:198px;top:0;width:194px;height:146px;"></div>
  <div class="photo photo--sunset" role="img" aria-label="Sunset over a lake" style="left:198px;top:149px;width:95px;height:70px;"></div>
  <div class="photo photo--path" role="img" aria-label="Country path and mountains" style="left:297px;top:149px;width:95px;height:70px;"></div>
</section>

<!-- Slide 3 -->
<section class="slide col-3 row-1">
  <div class="photo photo--golden" role="img" aria-label="Golden rolling hills under blue sky" style="inset:0;"></div>
  <svg width="392" height="219" style="position:absolute;inset:0;" aria-hidden="true"><path d="M202 0 Q215 150 310 219 L392 219 L392 0 Z" fill="var(--white)"/></svg>
  <p class="headline headline--right" style="position:absolute;right:16px;top:38px;width:150px;font-size:14px;">Flexibility, Innovation And Future Focus/Vision Are What Our Clients Can Count On Us For.</p>
</section>

<!-- Slide 4 -->
<section class="slide col-1 row-2">
  <div class="photo photo--lake" role="img" aria-label="Blue river beneath snowy mountains" style="left:0;top:0;width:392px;height:109px;"></div>
  <p class="headline headline--center" style="position:absolute;left:0;right:0;top:122px;padding:0 40px;">Work Is One Of Many Of Life's Great Facilitators, We Recognise And Value The Others - Its Not Just About Work.</p>
</section>

<!-- Slide 5 -->
<section class="slide col-2 row-2">
  <p class="lorem" style="position:absolute;left:34px;top:30px;width:130px;color:var(--green-text);">Lorem ipsum dolor sit amet, consectetur adipiscing elit. Nam leo nisi, mattis et nulla vitae, lacinia efficitur justo. Donec volutpa.</p>
  <div class="skill" style="top:113px;"><div class="skill__label">Marketing</div><div class="skill__track"><div class="skill__fill" style="width:90%;"></div></div><span class="skill__value">90%</span></div>
  <div class="skill" style="top:133px;"><div class="skill__label">Communication</div><div class="skill__track"><div class="skill__fill" style="width:85%;"></div></div><span class="skill__value">85%</span></div>
  <div class="skill" style="top:154px;"><div class="skill__label">Management</div><div class="skill__track"><div class="skill__fill" style="width:95%;"></div></div><span class="skill__value">95%</span></div>
  <div class="brand" style="left:8px;top:195px;color:var(--green-text);font-size:12px;"><span class="brand__dot" style="background:var(--green);"></span>northfield</div>
  <div style="position:absolute;left:20px;top:213px;width:165px;height:1.5px;background:var(--green);"></div>
  <div class="photo photo--portrait" role="img" aria-label="Portrait of a team member in a suit" style="left:185px;top:0;width:97px;height:219px;"></div>
  <div class="green-panel" style="left:282px;top:0;width:110px;height:219px;">
    <p style="position:absolute;left:17px;bottom:14px;font-size:18px;line-height:1.3;">Jonathan<br>Doe</p>
  </div>
</section>

<!-- Slide 6 -->
<section class="slide col-3 row-2">
  <div class="photo photo--waterfall" role="img" aria-label="Waterfall over a cliff" style="left:0;top:0;width:98px;height:107px;"></div>
  <div class="photo photo--cliff" role="img" aria-label="Waterfall pool in green forest" style="left:0;top:110px;width:98px;height:109px;"></div>
  <div class="photo photo--cliff" role="img" aria-label="Mossy cliff face" style="left:102px;top:0;width:97px;height:219px;"></div>
  <p class="headline" style="position:absolute;left:223px;top:34px;width:160px;">Flexibility, Innovation And Future Focus/Vision Are What Our Clients Can Count On Us For.</p>
</section>

<!-- Slide 7 -->
<section class="slide col-1 row-3">
  <div class="photo photo--path" role="img" aria-label="Path through rocky grassland" style="left:0;top:0;width:195px;height:145px;"></div>
  <div class="photo photo--valley" role="img" aria-label="Brown mountains and grass" style="left:199px;top:0;width:94px;height:145px;"></div>
  <div class="photo photo--valley" role="img" aria-label="Trees below mountains" style="left:297px;top:0;width:95px;height:145px;"></div>
  <div class="green-band caption" style="left:0;top:150px;width:392px;height:69px;display:flex;align-items:center;justify-content:center;text-align:center;padding:0 50px;">Work Is One Of Many Of Life's Great Facilitators, We Recognise And Value The Others - Its Not Just About Work.</div>
</section>

<!-- Slide 8 -->
<section class="slide col-2 row-3">
  <svg width="34" height="26" viewBox="0 0 34 26" style="position:absolute;left:38px;top:74px;" aria-hidden="true" fill="none" stroke="var(--green)" stroke-width="1.3" stroke-linejoin="round">
    <path d="M2 10 L8 3 L13 7 M32 10 L26 3 L18 6 L12 12 L15 14 L20 10 L28 18 L22 24 L12 15"/>
    <path d="M4 12 L14 22 L17 19 M8 8 L18 18"/>
  </svg>
  <p class="section-title" style="position:absolute;left:35px;top:101px;">Secret Bargains for Members</p>
  <p class="lorem" style="position:absolute;left:35px;top:118px;width:140px;line-height:2.6;">Lorem ipsum dolor sit amet, consectetur adipiscing elit. Nam leo nisi, mattis et nulla vitae, lacinia efficitur justo. Donec volutpa.</p>
  <svg width="392" height="219" style="position:absolute;inset:0;" role="img" aria-label="Close-up of frost crystals on moss">
    <defs><radialGradient id="frost" cx="65%" cy="55%" r="55%"><stop offset="0" stop-color="#e9eef0"/><stop offset=".45" stop-color="#9aa69c"/><stop offset=".8" stop-color="#3d5a2c"/><stop offset="1" stop-color="#243a1c"/></radialGradient></defs>
    <path d="M190 219 Q200 50 392 0 L392 219 Z" fill="url(#frost)"/>
  </svg>
</section>

<!-- Slide 9 -->
<section class="slide col-3 row-3">
  <svg width="30" height="24" viewBox="0 0 30 24" style="position:absolute;left:46px;top:78px;" aria-hidden="true">
    <ellipse cx="12" cy="10" rx="11" ry="8.5" fill="var(--green)"/>
    <path d="M4 15 L2 22 L10 17 Z" fill="var(--green)"/>
    <path d="M18 3 A10 8 0 0 1 28 12 L29 18 L24 15" fill="none" stroke="var(--green)" stroke-width="1.6"/>
  </svg>
  <p class="section-title" style="position:absolute;left:46px;top:104px;font-size:10px;">Secret Bargains for Members</p>
  <p class="lorem" style="position:absolute;left:46px;top:120px;width:135px;font-size:6px;line-height:2.6;">Lorem ipsum dolor sit amet, consectetur adipiscing elit. Nam leo nisi, mattis et nulla vitae, lacinia efficitur justo. Donec volutpa.</p>
  <svg width="392" height="219" style="position:absolute;inset:0;" role="img" aria-label="Mountain reflected in a still lake with a bird overhead">
    <defs><linearGradient id="reflect" x1="0" y1="0" x2="0" y2="1"><stop offset="0" stop-color="#c7c9c6"/><stop offset=".35" stop-color="#6f7367"/><stop offset=".55" stop-color="#3a4a5a"/><stop offset=".75" stop-color="#7d8a96"/><stop offset="1" stop-color="#3a3e42"/></linearGradient></defs>
    <path d="M190 0 L392 0 L392 219 Q220 210 190 0 Z" fill="url(#reflect)"/>
  </svg>
</section>

<!-- Slide 10 -->
<section class="slide col-1 row-4">
  <div class="photo photo--reflect" role="img" aria-label="Mountain reflected in lake" style="left:0;top:0;width:128px;height:107px;"></div>
  <div class="photo photo--rocks" role="img" aria-label="Rocky hills in sunlight" style="left:0;top:111px;width:128px;height:108px;"></div>
  <div class="green-panel" style="left:132px;top:0;width:128px;height:219px;">
    <p style="position:absolute;left:9px;top:74px;font-size:17.6px;line-height:1.25;">We Think Life Is About People And Relationships</p>
  </div>
  <div class="photo photo--peak" role="img" aria-label="Mountain over island cabins" style="left:264px;top:0;width:128px;height:107px;"></div>
  <div class="photo photo--sunset" role="img" aria-label="Golden hill over calm water" style="left:264px;top:111px;width:128px;height:108px;"></div>
</section>

<!-- Slide 11 -->
<section class="slide col-2 row-4">
  <div class="photo photo--rocks" role="img" aria-label="Rocky outcrop" style="left:0;top:0;width:128px;height:71px;"></div>
  <div class="photo photo--peak" role="img" aria-label="Fjord between cliffs" style="left:132px;top:0;width:128px;height:71px;"></div>
  <div class="photo photo--lighthouse" role="img" aria-label="Lighthouse on a headland" style="left:264px;top:0;width:128px;height:71px;"></div>
  <div class="photo photo--valley" role="img" aria-label="Green hills" style="left:0;top:75px;width:128px;height:70px;"></div>
  <div class="green-panel caption" style="left:132px;top:75px;width:260px;height:70px;padding:11px 8px;">Work Is One Of Many Of Life's Great Facilitators, We Recognise And Value The Others - Its Not Just About Work.</div>
  <div class="photo photo--coast" role="img" aria-label="Surf beach" style="left:0;top:149px;width:128px;height:70px;"></div>
  <div class="photo photo--snow" role="img" aria-label="Snowy mountains" style="left:132px;top:149px;width:128px;height:70px;"></div>
  <div class="photo photo--lake" role="img" aria-label="Lake and road" style="left:264px;top:149px;width:128px;height:70px;"></div>
</section>

<!-- Slide 12 -->
<section class="slide col-3 row-4">
  <div class="green-band" style="left:0;top:0;width:392px;height:71px;display:flex;align-items:center;justify-content:center;text-align:center;font-size:17.6px;line-height:1.25;padding:0 60px;">Flexibility, Innovation And Future Focus/Vision</div>
  <div class="photo photo--meadow" role="img" aria-label="Wildflowers before a volcano" style="left:0;top:75px;width:128px;height:144px;"></div>
  <div class="photo photo--meadow" role="img" aria-label="Volcano at dusk over meadow" style="left:132px;top:75px;width:128px;height:144px;"></div>
  <div class="photo photo--meadow" role="img" aria-label="Flowering grassland" style="left:264px;top:75px;width:128px;height:144px;"></div>
</section>

<!-- Slide 13 -->
<section class="slide col-2 row-5">
  <div class="green-panel" role="img" aria-label="Faint mountain range under green wash" style="inset:0;background:linear-gradient(180deg,#55ad4a 0%,#3ea63c 50%,#43ab3c 100%);"></div>
  <div class="brand" style="left:95px;top:171px;color:var(--white);font-size:15px;"><span class="brand__dot" style="background:var(--white);width:12px;height:12px;"></span>northfield</div>
  <p style="position:absolute;left:245px;top:162px;color:var(--white);font-family:'Oswald',sans-serif;font-weight:500;font-size:22px;letter-spacing:.3px;">THANK YOU...</p>
  <div style="position:absolute;left:100px;top:191px;width:292px;height:1.5px;background:var(--white);"></div>
</section>

</body>
</html>
```